Construction business card

I need a new business card, they can connect with my logo, brand.
What we do is residential house , design and build
I like: Navy blue / black
I attached our logo, brand,
and, some idea for business card.

```html
<!DOCTYPE html>
<html lang="en">
<head>
<meta charset="utf-8">
<title>Harlow Building Group – Business Card</title>
<link rel="stylesheet" href="https://fonts.googleapis.com/css2?family=Prompt:wght@500&family=Arimo:wght@400;700&display=swap">
<style>
  :root {
    --stage: #c4dfe0;
    --card-navy: #020a24;
    --accent-blue: #3f86d1;
    --mid-blue: #2a5ea8;
    --deep-blue: #14306a;
    --text-light: #e8eef7;
  }
  * { box-sizing: border-box; margin: 0; padding: 0; }
  html, body { width: 1200px; height: 1200px; overflow: hidden; }
  body {
    background: var(--stage);
    display: flex;
    flex-direction: column;
    align-items: center;
    justify-content: center;
    gap: 60px;
    font-family: "Arimo", Arial, sans-serif;
  }
  .card {
    position: relative;
    width: 820px;
    height: 500px;
    background: var(--card-navy);
    overflow: hidden;
    box-shadow: 0 18px 40px rgba(20, 50, 60, 0.25);
  }
  .card__decoration {
    position: absolute;
    right: 0;
    bottom: 0;
  }
  .card--front .card__decoration {
    width: 520px;
    height: 260px;
    background:
      linear-gradient(180deg, rgba(2, 10, 36, 0) 0%, rgba(20, 48, 106, 0.45) 60%, rgba(20, 48, 106, 0.6) 100%);
    -webkit-mask-image: linear-gradient(90deg, transparent 0%, #000 35%);
            mask-image: linear-gradient(90deg, transparent 0%, #000 35%);
  }
  .card--back .card__decoration {
    width: 640px;
    height: 400px;
    background:
      linear-gradient(200deg, rgba(2, 10, 36, 0) 0%, rgba(20, 48, 106, 0.7) 35%, rgba(42, 94, 168, 0.85) 60%, rgba(20, 48, 106, 0.75) 85%, rgba(2, 10, 36, 0.4) 100%);
    -webkit-mask-image: linear-gradient(90deg, transparent 0%, #000 30%);
            mask-image: linear-gradient(90deg, transparent 0%, #000 30%);
  }
  .brand {
    position: absolute;
    display: flex;
    align-items: center;
    gap: 14px;
    color: var(--accent-blue);
    font-family: "Arimo", Arial, sans-serif;
    font-weight: 700;
    text-transform: uppercase;
    line-height: 1.05;
  }
  .brand__square {
    width: 22px;
    height: 22px;
    background: var(--accent-blue);
    flex: none;
  }
  .card--front .brand { top: 120px; right: 56px; font-size: 30px; }
  .card--back .brand { top: 110px; left: 80px; font-size: 36px; }
  .holder {
    position: absolute;
    top: 110px;
    left: 0;
    padding-left: 62px;
  }
  .holder::before {
    content: "";
    position: absolute;
    left: 40px;
    top: 4px;
    width: 12px;
    height: 60px;
    border-radius: 0 4px 4px 0;
    background: var(--accent-blue);
  }
  .holder__name {
    font-family: "Prompt", sans-serif;
    font-weight: 500;
    font-size: 44px;
    line-height: 1;
    color: var(--accent-blue);
  }
  .holder__role {
    font-size: 15px;
    color: var(--text-light);
    margin-top: 4px;
  }
  .contact-list {
    position: absolute;
    left: 56px;
    top: 240px;
    list-style: none;
    color: var(--text-light);
    font-size: 19px;
    line-height: 1.3;
  }
  .contact-list li {
    display: flex;
    align-items: flex-start;
    gap: 22px;
    margin-bottom: 8px;
  }
  .contact-list li.contact--address { margin-bottom: 22px; }
  .contact-list svg {
    width: 20px;
    height: 20px;
    flex: none;
    margin-top: 2px;
    fill: none;
    stroke: var(--accent-blue);
    stroke-width: 2;
  }
</style>
</head>
<body>

<section class="card card--front">
  <div class="card__decoration" role="img" aria-label="Large faint roof-line graphic in deep blue"></div>

  <div class="holder">
    <h1 class="holder__name">Elias Marsh</h1>
    <p class="holder__role">Manager</p>
  </div>

  <ul class="contact-list">
    <li class="contact--address">
      <svg viewBox="0 0 20 20"><circle cx="10" cy="10" r="8"/><circle cx="10" cy="10" r="3" fill="var(--accent-blue)"/></svg>
      <span>42 Fernhill Street,<br>Eastvale, Vic 3190</span>
    </li>
    <li>
      <svg viewBox="0 0 20 20"><path d="M5 2l3 4-2 2c1 2 3 4 5 5l2-2 4 3-2 3C9 17 3 11 2 5z" fill="var(--accent-blue)" stroke="none"/></svg>
      <span>0400 555 018</span>
    </li>
    <li>
      <svg viewBox="0 0 20 20"><rect x="2" y="4" width="16" height="12"/><path d="M2 4l8 7 8-7"/></svg>
      <span>info@harlowbuildinggroup.com.au</span>
    </li>
    <li>
      <svg viewBox="0 0 20 20"><circle cx="10" cy="10" r="8"/><ellipse cx="10" cy="10" rx="3.5" ry="8"/><path d="M2 10h16M4 5.5h12M4 14.5h12"/></svg>
      <span>www.harlowbuildinggroup.com.au</span>
    </li>
  </ul>

  <div class="brand">
    <span class="brand__square"></span>
    <span>Harlow<br>Building Group</span>
  </div>
</section>

<section class="card card--back">
  <div class="card__decoration" role="img" aria-label="Large roof-line graphic in glowing blue across the lower right"></div>
  <div class="brand">
    <span class="brand__square"></span>
    <span>Harlow<br>Building Group</span>
  </div>
</section>

</body>
</html>
```